Website ui design required!

I require a web page ui design.
Theme: Outsourcing platform for developers and clients.
This website will be specifically for app/android/game/windows developers.
Anything that can be outsourced for app categories.
*App solutions
*Graphic design
*Marketing
*Project management
*mobile
*sdk intergration
*Developers
Basically if you want an app built on any platform, this website allows clients to connect with developers and other services surrounding that environment.
Please look at www.briskwork.com.au
Www.plorvin.com
Www.tefa.com
www.vormix.com
www.pellowind.com
Please make it look sleek and appealing.
I want this website to be the no.1 place for clients to source the best app developers worldwide. (random) I noticed these websites are 2 toned in color split, top and bottom.
All the best!!:)
Please take a look at the websites I mentioned.
Target Market(s)
Target market will be for anyone who wishes to
Find a developer, graphic artist, mobile apps, sdk integration,
app design, app consultation, web/mobile project management etc.
This is going to be an outsourcing platform for developers worldwide, also a place
For clients to hire manage and pay developers.
Industry/Entity Type
Graphic Design
Look and feel
Each slider illustrates characteristics of the customer's brand and the style your logo design should communicate.

```html
<!DOCTYPE html>
<html lang="en">
<head>
<meta charset="utf-8">
<title>devora – app outsourcing</title>
<link href="https://fonts.googleapis.com/css2?family=Comfortaa:wght@400;700&family=Arimo:wght@400;700&display=swap" rel="stylesheet">
<style>
  :root{
    --header:#7e1e17;
    --hero:#d4391f;
    --hero-wave:#dc4728;
    --peach:#f5c6ab;
    --deep:#80180d;
    --accent:#f0a530;
    --arrow:#e8a83a;
    --ring:#7e2118;
    --ring-inner:#f6cdb8;
    --label:#f7d6c4;
    --ink-red:#b8200f;
    --light-text:#f6d8c8;
    --tab:#d8301a;
  }
  *{box-sizing:border-box;margin:0;padding:0}
  html,body{width:1055px;height:1200px;overflow:hidden;background:var(--peach)}
  .page{position:relative;width:1055px;height:1200px;font-family:"Arimo",Arial,sans-serif}
  .abs{position:absolute}

  /* header */
  .site-header{position:absolute;left:0;top:0;width:1055px;height:81px;background:var(--header)}
  .brand{position:absolute;left:20px;top:24px;display:flex;align-items:center;gap:8px;font-family:"Arimo",sans-serif;font-weight:700;font-size:28px;line-height:32px;color:#f7e2d6}
  .brand-mark{width:12px;height:12px;background:#f7e2d6;flex:none}
  .main-nav a{position:absolute;top:27px;font-family:"Comfortaa",sans-serif;font-size:23px;color:#f3d3c4;text-decoration:none}
  .auth{position:absolute;left:858px;top:19px;width:183px;height:37px;background:#d8341d;border-radius:3px;display:flex;box-shadow:inset 0 -2px 0 #a82514}
  .auth a{flex:1;display:flex;align-items:center;justify-content:center;color:#fff;font-weight:700;font-size:13px;text-decoration:none}
  .auth a+a{border-left:1px solid #a82514}

  /* hero */
  .hero{position:absolute;left:0;top:81px;width:1055px;height:572px;background:var(--hero);overflow:hidden}
  .equation{position:absolute;left:0;top:45px;width:1055px;text-align:center;font-family:"Comfortaa",sans-serif;font-size:46px;color:var(--light-text);word-spacing:18px}
  .equation b{font-weight:700}
  .ring{position:absolute;width:82px;height:82px;border-radius:50%;background:var(--ring)}
  .ring::after{content:"";position:absolute;left:13px;top:13px;width:62px;height:62px;border-radius:50%;background:var(--ring-inner)}
  .ring-label{position:absolute;font-family:"Comfortaa",sans-serif;font-weight:700;font-size:17px;color:var(--label);text-shadow:0 0 2px #7e2118,1px 1px 0 #7e2118,-1px -1px 0 #7e2118;text-transform:uppercase;white-space:nowrap;z-index:2}
  .devices{position:absolute;left:404px;top:194px;width:229px;height:153px;border-radius:6px;background:linear-gradient(135deg,#8a2116,#b5462a 60%,#e2a33a)}
  .tagline{position:absolute;left:0;top:365px;width:1055px;text-align:center;font-family:"Comfortaa",sans-serif;font-size:44px;line-height:52px;color:var(--light-text)}
  .hero-copy{position:absolute;left:0;top:478px;width:1055px;text-align:center;font-size:15px;line-height:19px;color:#f4c3ad}

  /* project section */
  .intro{position:absolute;left:0;top:653px;width:1055px;height:273px;background:var(--peach)}
  .intro-lead{position:absolute;left:23px;top:30px;font-family:"Comfortaa",sans-serif;font-size:23px;color:var(--ink-red)}
  .post-cta{position:absolute;left:23px;top:74px;font-family:"Comfortaa",sans-serif;font-size:34px;color:var(--ink-red);display:flex;align-items:center;gap:8px}
  .category-tab{position:absolute;left:20px;top:136px;width:290px;height:37px;background:var(--tab);border-radius:0 12px 12px 0;color:#fbe1d3;font-family:"Comfortaa",sans-serif;font-size:17px;line-height:37px;padding-left:18px}
  .category-list{position:absolute;top:182px;list-style:none;font-size:15px;line-height:18px;color:var(--ink-red)}
  .category-list li::before{content:"⌐";font-size:11px;margin-right:7px;position:relative;top:-3px}
  .feature{position:absolute;left:632px;width:400px;display:flex;align-items:center}
  .feature svg{flex:none}
  .feature p{position:absolute;left:92px;font-size:13px;line-height:15px;color:var(--ink-red);width:300px}
  .dollar{font-family:"Arimo",sans-serif;font-weight:700;font-size:52px;color:#a7240f;width:69px;text-align:center}

  /* footer */
  .site-footer{position:absolute;left:0;top:926px;width:1055px;height:206px;background:var(--deep)}
  .footer-col{position:absolute;top:39px}
  .footer-col h3{font-size:19px;font-weight:700;color:var(--accent);margin-bottom:8px}
  .footer-col a{display:block;font-size:13px;line-height:16px;color:#f3d6c8;text-decoration:none}
  .socials{display:flex;gap:11px}
  .socials span{width:19px;height:19px;border-radius:2px;background:#3f86c6}
  .socials span:last-child{background:#f29b30}

  /* bottom bar */
  .bottom-bar{position:absolute;left:0;top:1132px;width:1055px;height:68px;background:var(--peach)}
  .bottom-brand{position:absolute;left:36px;top:25px;display:flex;align-items:center;gap:6px;font-family:"Arimo",sans-serif;font-weight:700;font-size:19px;line-height:22px;color:#8a1e12}
  .bottom-brand .brand-mark{width:9px;height:9px;background:#8a1e12}
  .copyright{position:absolute;left:132px;top:29px;font-size:13px;color:#5a150d}
  .trust-badge{position:absolute;left:800px;top:14px;width:92px;height:40px;border-radius:20px;border:3px solid #7e1e17}
  .pay-name{position:absolute;left:920px;top:14px;font-family:"Arimo",sans-serif;font-weight:700;font-size:32px;color:#7e1e17}
</style>
</head>
<body>
<div class="page">

  <header class="site-header">
    <div class="brand"><span class="brand-mark"></span>devora</div>
    <nav class="main-nav">
      <a style="left:202px">app employers</a>
      <a style="left:440px">app masters</a>
      <a style="left:658px">why devora</a>
    </nav>
    <div class="auth"><a>SIGNUP</a><a>LOG IN</a></div>
  </header>

  <section class="hero">
    <svg class="abs" style="left:0;top:0" width="1055" height="572" viewBox="0 0 1055 572">
      <path d="M0 0H1055V95C950 40 820 40 690 80C560 120 430 125 300 95C180 65 80 65 0 110Z" fill="var(--hero-wave)"/>
      <defs>
        <marker id="head" viewBox="0 0 10 10" refX="8" refY="5" markerWidth="4" markerHeight="4" orient="auto">
          <path d="M0 0L10 5L0 10L3 5Z" fill="var(--arrow)"/>
        </marker>
      </defs>
      <g stroke="var(--arrow)" stroke-width="6" fill="none" marker-end="url(#head)" stroke-linecap="round">
        <line x1="210" y1="183" x2="335" y2="228"/>
        <line x1="135" y1="280" x2="340" y2="269"/>
        <line x1="183" y1="393" x2="367" y2="315"/>
        <line x1="829" y1="183" x2="700" y2="228"/>
        <line x1="931" y1="280" x2="708" y2="266"/>
        <line x1="877" y1="403" x2="690" y2="322"/>
      </g>
    </svg>
    <div class="equation">app + <b>APP</b> = app</div>

    <div class="ring" style="left:101px;top:115px"></div>
    <div class="ring-label" style="left:130px;top:146px">Solutions</div>
    <div class="ring" style="left:37px;top:266px"></div>
    <div class="ring-label" style="left:66px;top:297px">Graphic Design</div>
    <div class="ring" style="left:126px;top:402px"></div>
    <div class="ring-label" style="left:155px;top:433px">Mobile</div>
    <div class="ring" style="left:856px;top:122px"></div>
    <div class="ring-label" style="left:704px;top:153px">Project Management</div>
    <div class="ring" style="left:942px;top:258px"></div>
    <div class="ring-label" style="left:842px;top:289px">SDK Intergration</div>
    <div class="ring" style="left:869px;top:402px"></div>
    <div class="ring-label" style="left:811px;top:433px">Developers</div>

    <div class="devices" role="img" aria-label="Illustration of a desktop monitor showing a group of people, with a tablet and phone beside it"></div>

    <div class="tagline">all gather in<br>one place</div>
    <p class="hero-copy">If you want an app built on any platform, devora allows clients<br>to connect with developers and other services surrounding that environment.</p>
  </section>

  <section class="intro">
    <p class="intro-lead">posting a project is easy and free!</p>
    <div class="post-cta">
      <svg width="28" height="30" viewBox="0 0 28 30"><path d="M4 2V20H20" stroke="var(--ink-red)" stroke-width="5" fill="none"/><path d="M18 12L27 20L18 28Z" fill="var(--ink-red)"/></svg>
      POST PROJECT NOW
    </div>
    <div class="category-tab">Explore top App Categories</div>
    <ul class="category-list" style="left:27px">
      <li>APP Solutions</li><li>Graphic Design</li><li>Marketing</li><li>Project Management</li>
    </ul>
    <ul class="category-list" style="left:231px">
      <li>Mobile</li><li>SDK Integration</li><li>Developers</li>
    </ul>

    <div class="feature" style="top:34px">
      <svg width="69" height="46" viewBox="0 0 69 46"><rect x="9" y="2" width="51" height="34" rx="3" fill="#a7240f"/><rect x="0" y="38" width="69" height="6" rx="2" fill="#a7240f"/></svg>
      <p>Build a flexible workforce based on skills, ratings, and reviews.</p>
    </div>
    <div class="feature" style="top:116px">
      <svg width="69" height="48" viewBox="0 0 69 48"><path d="M2 0V46H69" stroke="#a7240f" stroke-width="4" fill="none"/><rect x="10" y="22" width="11" height="22" fill="#a7240f"/><rect x="25" y="28" width="11" height="16" fill="#a7240f"/><rect x="40" y="16" width="11" height="28" fill="#a7240f"/><rect x="55" y="8" width="11" height="36" fill="#a7240f"/></svg>
      <p>See work-in-progress screenshots, time sheets, and daily logs.</p>
    </div>
    <div class="feature" style="top:194px">
      <div class="dollar">$</div>
      <p>Rest assured with safe global payments and the devora Guarantee.</p>
    </div>
  </section>

  <footer class="site-footer">
    <div class="footer-col" style="left:38px"><h3>Navigate</h3><a>Home</a><a>Why devora</a><a>Take the Tour</a><a>Who's Using It</a></div>
    <div class="footer-col" style="left:231px"><h3>Take Action</h3><a>Post Project</a><a>Sign in</a><a>Register</a><a>Search for Freelancers</a><a>Ask a Question</a></div>
    <div class="footer-col" style="left:456px"><h3>Resources</h3><a>About Tefa</a><a>Answers</a><a>Blog</a><a>Help</a><a>Directory</a></div>
    <div class="footer-col" style="left:672px"><h3>Necessities</h3><a>IP Policy</a><a>Privacy Policy</a><a>Terms of Service</a></div>
    <div class="footer-col" style="left:898px"><h3>Our Socials</h3><div class="socials"><span></span><span></span><span></span><span></span></div></div>
  </footer>

  <div class="bottom-bar">
    <div class="bottom-brand"><span class="brand-mark"></span>devora</div>
    <p class="copyright">© 2003-2013 devora Corporation.</p>
    <div class="trust-badge"></div>
    <div class="pay-name">Payvale</div>
  </div>

</div>
</body>
</html>
```